Sleek business card design for digital agency.

Brief document attached for detailed description and inspiration. Looking for a minimalist sleek, cool, modern business card design.

Industry/Entity Type

Digital

```html
<!DOCTYPE html>
<html lang="en">
<head>
<meta charset="utf-8">
<title>Flint Works – Business Card</title>
<link rel="stylesheet" href="https://fonts.googleapis.com/css2?family=Open+Sans:wght@400;600;700&display=swap">
<style>
  :root {
    --backdrop: #e6e6e6;
    --card: #262626;
    --card-edge: #1c1c1c;
    --accent: #2a9fd8;
    --text-soft: #b9b9b9;
    --text-muted: #8e8e8e;
    --decor: #2f2f2f;
    --logo-ink: #161616;
  }
  * { box-sizing: border-box; margin: 0; padding: 0; }
  html, body {
    width: 1200px; height: 961px; overflow: hidden;
    background: var(--backdrop);
    font-family: "Open Sans", sans-serif;
  }
  .stage {
    width: 1200px; height: 961px;
    display: flex; flex-direction: column;
    align-items: center; justify-content: center; gap: 60px;
  }
  .card {
    position: relative;
    width: 640px; height: 360px;
    background: var(--card);
    border-radius: 28px;
    border: 1px solid var(--card-edge);
    overflow: hidden;
  }
  .card-front .decor-mark {
    position: absolute; left: 250px; top: 60px;
    width: 230px; height: 230px; border-radius: 50%;
    background: radial-gradient(circle, var(--decor) 0%, rgba(47,47,47,0) 70%);
  }
  .drink-order {
    position: absolute; right: 48px; top: 44px;
    text-align: right; color: var(--text-soft);
    font-size: 14px; line-height: 1.45; letter-spacing: 0.5px;
  }
  .identity { position: absolute; left: 48px; top: 96px; }
  .identity .name {
    color: var(--accent); font-weight: 700;
    font-size: 22px; letter-spacing: 1px; text-transform: uppercase;
  }
  .identity .role { color: var(--text-soft); font-size: 15px; margin-top: 2px; }
  .contacts {
    position: absolute; left: 48px; top: 168px;
    list-style: none; color: var(--text-soft);
    font-size: 14px; line-height: 20px;
  }
  .contacts li { display: flex; align-items: center; gap: 12px; }
  .contacts svg { width: 14px; height: 14px; flex: none; }
  .address {
    position: absolute; left: 48px; bottom: 34px;
    color: var(--text-muted); font-size: 13.5px; line-height: 1.45;
  }
  .card-back { display: flex; align-items: center; justify-content: center; }
  .brand { display: flex; align-items: center; gap: 18px; }
  .brand-dot { width: 44px; height: 44px; border-radius: 50%; background: var(--logo-ink); }
  .brand-name {
    color: var(--logo-ink); font-weight: 700; font-size: 62px; letter-spacing: -1px;
  }
</style>
</head>
<body>
<main class="stage">
  <section class="card card-front">
    <div class="decor-mark" role="img" aria-label="Faint brand emblem illustration"></div>
    <p class="drink-order">DRINK ORDER:<br>G&amp;T with cucumber</p>
    <div class="identity">
      <h1 class="name">Daniel Hart</h1>
      <p class="role">Marketing Director</p>
    </div>
    <ul class="contacts">
      <li><svg viewBox="0 0 14 14"><circle cx="7" cy="7" r="7" fill="var(--accent)"/><path d="M4.5 3.5l1.5 0 .6 1.8-.9.7a5 5 0 0 0 2.3 2.3l.7-.9 1.8.6v1.5c0 .4-.4.7-.8.6A6 6 0 0 1 3.9 4.3c-.1-.4.2-.8.6-.8z" fill="var(--card)"/></svg>0400 218 706</li>
      <li><svg viewBox="0 0 14 14"><circle cx="7" cy="7" r="7" fill="var(--accent)"/><path d="M4.5 3.5l1.5 0 .6 1.8-.9.7a5 5 0 0 0 2.3 2.3l.7-.9 1.8.6v1.5c0 .4-.4.7-.8.6A6 6 0 0 1 3.9 4.3c-.1-.4.2-.8.6-.8z" fill="var(--card)"/></svg>03 9120 4488</li>
      <li><svg viewBox="0 0 14 14"><circle cx="7" cy="7" r="7" fill="var(--accent)"/></svg>dhart@flintworks.com</li>
      <li><svg viewBox="0 0 14 14"><circle cx="7" cy="7" r="7" fill="var(--accent)"/></svg>www.flintworks.com</li>
      <li><svg viewBox="0 0 14 14"><circle cx="7" cy="7" r="7" fill="var(--accent)"/></svg>social.flintworks.com</li>
      <li><svg viewBox="0 0 14 14"><circle cx="7" cy="7" r="7" fill="var(--accent)"/></svg>@dhart82</li>
    </ul>
    <p class="address">Level 2, 18 Harlow St<br>East Marden NSW 5100</p>
  </section>

  <section class="card card-back">
    <div class="brand">
      <span class="brand-dot"></span>
      <span class="brand-name">Flint Works</span>
    </div>
  </section>
</main>
</body>
</html>
```